Motorcycle dealer home page design (Lone Canyon Cycle Depot - 4341)

We need a home page design only (no coding necessary) for a motorcycle dealer. He wants the theme to be Modern-Industrial with vintage details. Please read the requirements below.

Client likes http://www.pelbrookridgeriders.example/ and wants a similar layout.

Dealer info:
Lone Canyon Cycle Depot (logo attached)
210.555.0147
628 W Maple Crest Dr Ste 307
San Antonio, TX 78299
Hours
Sun-Mon: Closed
Tue-Sat: 9a – 6p

Slideshow images - I've attached a few so you can see his inventory, it may help with the design

Call-to-action buttons:
Financing
Sell Your Bike
View Inventory

Theme: Modern-Industrial with Vintage details
Main background: Artistic or vintage image of motorcycle (see link for examples from client: http://instagram.com/chromeandember#)
Content background: likes the use of 'black wood' on http://www.pelbrookridgeriders.example - find a way to incorporate the wood background somewhere on the design

Accent Colors: Black, white and pops of red
Featured Vehicles location: Middle (in between the call-to-action buttons and the verbiage)
Social Networking: Facebook, Instagram

Client likes http://www.pelbrookridgeriders.example/ and wants a similar layout:
-wants the navigation bar above the banner/header
-wants the logo centered in the banner/header (open to the placement of the phone number, address and social media icons, as long as they show in the banner)
-wants to leave gaps between the sections so the background is visible

Attachments:
-layout that the client provided (LCD_HOME_PAGE)
-logo (LCD_BLACK & LCD_W)
-psd file showing the typical layout used (sample-site) - ONLY A SUGGESTION!
-a few slideshow images to show client's inventory (the rest of the files)

Please let me know if you have any questions and thank you in advance for your work.

Thank you all for your wonderful mockups. I've sent them to the client and am awaiting the response. I will keep you all updated. Best regards, Delphine

Thank you all, I am just waiting for feedback from the client. I will post the feedback as soon as I get a response from the client. Best regards, Delphine

```html
<!DOCTYPE html>
<html lang="en">
<head>
<meta charset="utf-8">
<title>Lone Canyon Cycle Depot</title>
<link href="https://fonts.googleapis.com/css2?family=Lato:wght@300;400;700;900&display=swap" rel="stylesheet">
<style>
:root{
  --ink:#070707;
  --panel:#121212;
  --line:#2c2c2c;
  --text:#d8d8d8;
  --muted:#8f8f8f;
  --white:#ffffff;
  --red:#c4262b;
}
*{box-sizing:border-box;margin:0;padding:0}
html,body{width:798px;height:1200px;overflow:hidden;background:var(--ink)}
body{font-family:'Lato',sans-serif;color:var(--text);position:relative}
.page-backdrop{position:absolute;inset:0;
  background:
    radial-gradient(ellipse 220px 160px at 120px 150px,rgba(90,90,90,.35),transparent 70%),
    radial-gradient(ellipse 160px 300px at 60px 480px,rgba(70,70,70,.45),transparent 70%),
    radial-gradient(ellipse 260px 120px at 620px 160px,rgba(80,80,80,.3),transparent 70%),
    radial-gradient(ellipse 180px 260px at 740px 560px,rgba(75,75,75,.35),transparent 70%),
    radial-gradient(ellipse 300px 180px at 400px 760px,rgba(60,60,60,.3),transparent 70%),
    radial-gradient(ellipse 240px 200px at 150px 980px,rgba(65,65,65,.35),transparent 70%),
    radial-gradient(ellipse 260px 160px at 640px 1000px,rgba(60,60,60,.3),transparent 70%),
    linear-gradient(160deg,#1d1d1d 0%,#0d0d0d 40%,#141414 60%,#060606 100%)}
.abs{position:absolute}
.main-nav{left:107px;width:584px;top:31px;height:22px;border-top:1px solid var(--line);border-bottom:1px solid var(--line);display:flex;justify-content:space-between;align-items:center}
.main-nav a{font-size:7px;font-weight:700;color:var(--white);text-decoration:none;letter-spacing:.2px}
.main-nav a::before,.main-nav a::after{content:"\2605";color:var(--muted);font-size:5px;margin:0 5px}
.brand-mark{left:332px;top:81px;width:134px;height:68px;border:2px solid var(--white);border-radius:6px;background:var(--ink);display:flex;align-items:center;justify-content:center;text-align:center;font-weight:900;font-size:13px;line-height:1.1;color:var(--white);letter-spacing:.5px}
.header-phone{right:107px;top:94px;font-size:11px;color:var(--red);font-weight:300;display:flex;gap:6px;align-items:center}
.social{display:flex;gap:11px}
.social span{width:15px;height:15px;border:1px solid var(--muted);border-radius:50%;display:flex;align-items:center;justify-content:center}
.header-social{left:601px;top:120px}
.header-info{top:173px;left:275px;display:flex;gap:26px;font-size:8.5px;font-weight:300;line-height:12px;color:var(--text)}
.header-info div{display:flex;gap:6px}
.hero{left:107px;top:219px;width:584px;height:234px;background:linear-gradient(120deg,#9a9a9a 0%,#6d6d6d 35%,#2e2b3d 65%,#181818 100%)}
.hero-title{left:107px;top:330px;width:584px;text-align:center;font-weight:900;font-size:30px;color:#eeeeee;letter-spacing:1px}
.hero-sub{left:107px;top:372px;width:584px;text-align:center;font-weight:700;font-size:16px;color:#eeeeee;letter-spacing:4px}
.hero-arrow{top:325px;width:19px;height:19px;background:rgba(255,255,255,.35);display:flex;align-items:center;justify-content:center}
.hero-dots{left:300px;top:444px;width:180px;height:2px;background:rgba(255,255,255,.6)}
.cta{top:496px;height:33px;width:181px;border:2px solid #3a3a3a;background:var(--panel);display:flex;align-items:center;font-size:9.5px;font-weight:700;color:var(--white)}
.cta .ico{width:40px;height:100%;border-right:1px solid #3a3a3a;display:flex;align-items:center;justify-content:center}
.cta .label{flex:1;text-align:center}
.section-title{left:107px;width:584px;font-size:10.5px;font-weight:700;color:var(--white);border-bottom:2px solid var(--line);padding-bottom:7px}
.see-all{right:107px;top:591px;font-size:6.5px;color:var(--red);font-weight:700}
.bike-card{top:636px;width:185px}
.bike-photo{height:109px}
.bike-meta{margin-top:10px;font-size:7.5px;line-height:16px;color:var(--white);position:relative}
.bike-meta b{color:var(--red);font-weight:400}
.see-more{position:absolute;right:0;top:18px;border:2px solid #3a3a3a;padding:4px 8px;font-size:6.5px;font-weight:700;color:var(--white);line-height:10px}
.carousel-next{left:716px;top:683px;width:15px;height:15px;border:1px solid var(--muted);border-radius:50%;display:flex;align-items:center;justify-content:center}
.about{left:107px;top:897px;width:584px;font-size:8.3px;line-height:12px;color:var(--white);font-weight:400}
.about p{margin-bottom:12px}
.about a{color:var(--red);text-decoration:none}
.footer-rule{left:107px;top:1061px;width:584px;border-top:2px solid var(--line)}
.footer-logo{left:108px;top:1090px;width:134px;height:66px}
.footer-col{top:1085px;font-size:7.5px;line-height:12px;color:var(--text);font-weight:300}
.footer-col h4{font-size:10px;font-weight:700;color:var(--white);margin-bottom:14px}
.footer-col .row{display:flex;gap:6px;margin-bottom:4px}
.copyright{left:107px;top:1184px;font-size:6.5px;color:var(--muted)}
</style>
</head>
<body>
<div class="page-backdrop" role="img" aria-label="Dark moody close-up photograph of a motorcycle as page background"></div>

<nav class="main-nav abs">
  <a>HOME</a><a>ABOUT US</a><a>INVENTORY</a><a>FINANCING</a><a>LOCATION</a><a>CONTACT</a>
</nav>

<div class="brand-mark abs">LONE CANYON<br>CYCLE DEPOT</div>

<div class="header-phone abs">
  <svg width="9" height="9" viewBox="0 0 10 10"><path d="M2 1l2 2-1 1.5c.6 1.2 1.3 1.9 2.5 2.5L7 6l2 2-1.5 1.5C4 9 1 6 .5 2.5z" fill="#777"/></svg>
  210.555.0147
</div>
<div class="social header-social abs">
  <span><svg width="7" height="7" viewBox="0 0 10 10"><path d="M1 1h8v6H4L2 9V7H1z" fill="none" stroke="#999" stroke-width="1.2"/></svg></span>
  <span><svg width="7" height="7" viewBox="0 0 10 10"><path d="M5 9L1.5 5.5A2.2 2.2 0 0 1 5 2.5a2.2 2.2 0 0 1 3.5 3z" fill="none" stroke="#999" stroke-width="1.2"/></svg></span>
  <span><svg width="7" height="7" viewBox="0 0 10 10"><circle cx="5" cy="5" r="4" fill="none" stroke="#999" stroke-width="1.2"/><path d="M1 5h8M5 1v8" stroke="#999"/></svg></span>
  <span><svg width="7" height="6" viewBox="0 0 10 8"><rect x=".5" y=".5" width="9" height="7" fill="none" stroke="#999"/><path d="M.5 .5l4.5 4 4.5-4" stroke="#999" fill="none"/></svg></span>
</div>

<div class="header-info abs">
  <div><svg width="7" height="9" viewBox="0 0 8 10"><path d="M4 0a3.5 3.5 0 0 1 3.5 3.5C7.5 6 4 10 4 10S.5 6 .5 3.5A3.5 3.5 0 0 1 4 0z" fill="#ddd"/><circle cx="4" cy="3.5" r="1.2" fill="#111"/></svg><span>628 W Maple Crest Dr Ste 307<br>San Antonio, TX 78299</span></div>
  <div><svg width="8" height="8" viewBox="0 0 10 10"><circle cx="5" cy="5" r="4" fill="none" stroke="#ddd" stroke-width="1.5"/><path d="M5 2.5V5h2" stroke="#ddd" fill="none"/></svg><span>Tuesday - Saturday : 9a- 6p<br>Sunday - Monday: Closed</span></div>
</div>

<div class="hero abs" role="img" aria-label="Slideshow photo of a purple touring motorcycle parked by a garage door"></div>
<div class="hero-title abs">LONE CANYON CYCLE</div>
<div class="hero-sub abs">DEPOT</div>
<div class="hero-arrow abs" style="left:127px"><svg width="6" height="8"><path d="M5 0L1 4l4 4" stroke="#fff" fill="none" stroke-width="1.5"/></svg></div>
<div class="hero-arrow abs" style="left:652px"><svg width="6" height="8"><path d="M1 0l4 4-4 4" stroke="#fff" fill="none" stroke-width="1.5"/></svg></div>
<div class="hero-dots abs"></div>

<div class="cta abs" style="left:109px"><span class="ico"><svg width="9" height="11"><rect x=".5" y=".5" width="8" height="10" fill="none" stroke="#fff"/><rect x="2" y="2" width="5" height="2" fill="#fff"/><path d="M2 6h1M4 6h1M6 6h1M2 8h1M4 8h1M6 8h1" stroke="#fff"/></svg></span><span class="label">FINANCING</span></div>
<div class="cta abs" style="left:308px"><span class="ico"><svg width="9" height="12"><path d="M3 0h3L5 2a4 4.5 0 1 1-1 0z" fill="#fff"/></svg></span><span class="label">SELL YOUR BIKE</span></div>
<div class="cta abs" style="left:507px"><span class="ico"><svg width="13" height="13"><circle cx="5" cy="5" r="4" fill="none" stroke="#fff" stroke-width="1.6"/><path d="M8 8l4.5 4.5" stroke="#fff" stroke-width="2"/></svg></span><span class="label">VIEW INVENTORY</span></div>

<h2 class="section-title abs" style="top:588px">FEATURED MOTORCYCLES</h2>
<a class="see-all abs">SEE ALL BIKES</a>

<div class="bike-card abs" style="left:107px">
  <div class="bike-photo" role="img" aria-label="Photo of a chrome custom motorcycle" style="background:linear-gradient(135deg,#cfcfcf,#6c6c6c 60%,#3a3a3a)"></div>
  <div class="bike-meta"><b>BIKE NAME:</b> AMERICAN IPSUM<br><b>YEAR:</b> 2014<br><b>PRICE:</b> $25,000<span class="see-more">SEE MORE</span></div>
</div>
<div class="bike-card abs" style="left:307px">
  <div class="bike-photo" role="img" aria-label="Photo of a purple motorcycle tank and chrome gauges" style="background:linear-gradient(135deg,#d8d8d8,#8a8a8a 45%,#3b3550)"></div>
  <div class="bike-meta"><b>BIKE NAME:</b> AMERICAN IPSUM<br><b>YEAR:</b> 2014<br><b>PRICE:</b> $25,000<span class="see-more">SEE MORE</span></div>
</div>
<div class="bike-card abs" style="left:506px">
  <div class="bike-photo" role="img" aria-label="Photo of a red touring motorcycle fairing" style="background:linear-gradient(135deg,#e5e5e5,#b01d22 55%,#5a0c0f)"></div>
  <div class="bike-meta"><b>BIKE NAME:</b> AMERICAN IPSUM<br><b>YEAR:</b> 2014<br><b>PRICE:</b> $25,000<span class="see-more">SEE MORE</span></div>
</div>
<div class="carousel-next abs"><svg width="5" height="7"><path d="M1 0l3 3.5L1 7" stroke="#ccc" fill="none"/></svg></div>

<h2 class="section-title abs" style="top:852px">HIGH QUALITY PRE-OWNED MOTORCYCLES</h2>
<div class="about abs">
  <p>Lone Canyon Cycle Depot is the place to get the best pre-owned V-Twin cruisers, Bad-ass Baggers, and American made choppers in San Antonio, TX.</p>
  <p>We aim to be premier pre-owned motorcycle dealer of top quality V-Twin cruisers, custom cruisers, and just about anything 2 wheeled in San Antonio. We pride ourselves on finding quality motorcycles that we hand-pick. At Lone Canyon Cycle Depot, we want to watch each of our customers ride off on their new motorcycle with a smile on their face &amp; only the freedom of the open road on their mind.</p>
  <p>Come by and see us at Lone Canyon Cycle Depot in San Antonio, TX or check us out online at <a>LoneCanyonCycleDepot.example</a> We offer the best quality pre-owned V-Twins, bad-ass custom baggers, American-made choppers, clean sportbikes and just about anything else on two wheels!</p>
</div>

<div class="footer-rule abs"></div>
<div class="brand-mark footer-logo abs">LONE CANYON<br>CYCLE DEPOT</div>

<div class="footer-col abs" style="left:257px">
  <h4>Hours:</h4>
  <div class="row"><svg width="7" height="7" viewBox="0 0 10 10"><circle cx="5" cy="5" r="4" fill="none" stroke="#ddd" stroke-width="1.5"/><path d="M5 2.5V5h2" stroke="#ddd" fill="none"/></svg><span>Tuesday - Saturday : 9a - 6p<br>Sunday - Monday: Closed</span></div>
</div>
<div class="footer-col abs" style="left:406px">
  <h4>Contact:</h4>
  <div class="row"><svg width="6" height="8" viewBox="0 0 8 10"><path d="M4 0a3.5 3.5 0 0 1 3.5 3.5C7.5 6 4 10 4 10S.5 6 .5 3.5A3.5 3.5 0 0 1 4 0z" fill="#ddd"/></svg><span>628 W Maple Crest Dr Ste 307<br>San Antonio, TX 78299</span></div>
  <div class="row"><svg width="7" height="7" viewBox="0 0 10 10"><path d="M2 1l2 2-1 1.5c.6 1.2 1.3 1.9 2.5 2.5L7 6l2 2-1.5 1.5C4 9 1 6 .5 2.5z" fill="#ddd"/></svg><span>210.555.0147</span></div>
  <div class="row"><svg width="7" height="6" viewBox="0 0 10 8"><rect width="10" height="8" fill="#ddd"/><path d="M0 0l5 4 5-4" stroke="#111" fill="none"/></svg><span style="font-size:6.5px">sales@lonecanyoncycledepot.example</span></div>
</div>
<div class="footer-col abs" style="left:556px">
  <h4>Find Us:</h4>
  <div class="social">
    <span><svg width="7" height="7" viewBox="0 0 10 10"><path d="M1 1h8v6H4L2 9V7H1z" fill="none" stroke="#999" stroke-width="1.2"/></svg></span>
    <span><svg width="7" height="7" viewBox="0 0 10 10"><path d="M5 9L1.5 5.5A2.2 2.2 0 0 1 5 2.5a2.2 2.2 0 0 1 3.5 3z" fill="none" stroke="#999" stroke-width="1.2"/></svg></span>
    <span><svg width="7" height="7" viewBox="0 0 10 10"><circle cx="5" cy="5" r="4" fill="none" stroke="#999" stroke-width="1.2"/><path d="M1 5h8M5 1v8" stroke="#999"/></svg></span>
    <span><svg width="7" height="6" viewBox="0 0 10 8"><rect x=".5" y=".5" width="9" height="7" fill="none" stroke="#999"/><path d="M.5 .5l4.5 4 4.5-4" stroke="#999" fill="none"/></svg></span>
  </div>
</div>

<div class="copyright abs">Copyright © 2014 Lone Canyon Cycle Depot. All Rights Reserved.</div>
</body>
</html>
```